WordPress Coding + Design - Website designed to maximise leads required

Please see the velmot brief.doc file

it is VERY important that this website be DESIGNED with MOBILE + TABLET BOOTSTRAP in mind.

The design has to look amazing on mobile and tablet.

Reason: Designer failed to meet expectations and wasted my time

Number of Pages Required

1 page

```html
<!DOCTYPE html>
<html lang="en">
<head>
<meta charset="utf-8">
<title>Velmot College Advisors</title>
<link href="https://fonts.googleapis.com/css2?family=Open+Sans:ital,wght@0,400;0,600;0,700;1,400&display=swap" rel="stylesheet">
<style>
:root{
  --navy:#1c2a6e;
  --navy-dark:#142058;
  --orange:#d99a22;
  --ink:#222;
  --text:#555;
  --muted:#777;
  --rule:#dcdcdc;
  --panel:#ececec;
  --bar:#0d0d0d;
  --footer:#151515;
  --footer-text:#9a9a9a;
}
*{margin:0;padding:0;box-sizing:border-box}
html,body{width:1200px;height:3120px;overflow:hidden}
body{font-family:'Open Sans',Arial,sans-serif;color:var(--text);background:#fff;position:relative}
.abs{position:absolute}
a{color:inherit;text-decoration:none}

/* header */
.brand{left:100px;top:26px;display:flex;align-items:center;gap:14px}
.brand-dot{width:62px;height:62px;border-radius:50%;background:var(--navy)}
.brand-name{font-size:40px;font-weight:700;color:var(--navy);letter-spacing:1px}
.social{left:928px;top:24px;display:flex;gap:6px}
.social span{width:22px;height:22px;background:#8d8d8d;border-radius:3px;display:block}
.lang{left:1022px;top:24px;width:80px;height:24px;border:1px solid #ccc;font-size:12px;color:#777;padding:3px 0 0 16px}
.lang::after{content:"";position:absolute;right:12px;top:8px;border:5px solid transparent;border-top-color:#999}
.contact-line{top:70px;right:100px;display:flex;gap:30px;font-size:13px;color:#444;align-items:center}
.contact-line span{display:flex;align-items:center;gap:8px}
.nav{top:114px;left:0;width:1200px;height:52px;background:var(--bar);border-top:4px solid var(--orange);display:flex;justify-content:space-between;align-items:center;padding:0 128px 0 124px}
.nav a{color:#fff;font-size:13px;font-weight:600}
.nav a.active{color:var(--orange)}

/* hero */
.hero{top:166px;left:0;width:1200px;height:490px;background:linear-gradient(100deg,#6b4a35 0%,#c79778 25%,#e8c3a6 42%,#8a5a3f 60%,#c8432f 80%,#7a2a22 100%);overflow:hidden}
.hero-caption{left:601px;top:156px;width:499px;height:181px;background:rgba(36,48,130,.88);border:2px solid rgba(255,255,255,.5);color:#fff;font-size:52px;line-height:62px;padding:22px 0 0 14px}
.hero-arrow{top:195px;width:44px;height:44px;border:3px solid #fff;border-radius:50%}
.hero-curve{left:0;bottom:0}

/* features */
.feature{top:713px;width:312px}
.feature-head{height:38px;background:var(--panel);display:flex;align-items:center}
.feature-icon{width:50px;height:38px;background:var(--navy);display:flex;align-items:center;justify-content:center}
.feature-head h3{font-size:17px;font-weight:600;color:var(--navy);margin-left:22px}
.feature .tag{font-size:11.5px;font-style:italic;color:var(--orange);margin:16px 0 8px}
.feature p.body{font-size:13px;line-height:22px}
.more{display:block;font-size:11.5px;font-weight:700;color:var(--navy);margin-top:14px}
.rule{left:100px;width:1000px;height:1px;background:var(--rule)}
.section-title{font-size:30px;font-weight:600;color:var(--ink)}
.btn-small{background:var(--navy);color:#fff;font-size:11px;font-weight:700;width:84px;height:33px;display:flex;align-items:center;justify-content:center}

/* services */
.service{top:1009px;width:231px}
.service-photo{height:157px;border-top:4px solid #a8743a}
.service h4{font-size:18px;font-weight:400;color:var(--ink);margin:18px 0 12px;letter-spacing:.3px}
.service p{font-size:12.5px;line-height:23px}

/* news & testimonials */
.news-item{left:100px;width:440px}
.news-item h4{font-size:17px;font-weight:700;color:var(--navy)}
.news-date{font-size:12px;font-style:italic;color:var(--orange);display:flex;align-items:center;gap:8px;margin:8px 0 10px}
.news-item p{font-size:12.5px;line-height:24px}
.testimonial{left:605px;width:495px;display:flex;gap:22px}
.testimonial-photo{width:136px;height:115px;flex:none;border:1px solid #bbb}
.testimonial h5{font-size:13px;font-weight:700;color:var(--ink);margin-top:2px}
.testimonial p{font-size:12.5px;font-style:italic;line-height:22px;margin-top:14px}

/* admissions */
.video{left:98px;top:1866px;width:464px;height:266px;background:linear-gradient(160deg,#d8d4cc 0%,#9c958b 35%,#2a2a2e 70%,#15151a 100%);border:1px solid #888}
.admit{left:600px;top:1858px;width:500px}
.admit h2{font-size:31px;font-weight:400;line-height:46px;color:var(--ink)}
.admit p{font-size:12.5px;line-height:24px;color:var(--muted);margin:14px 0 24px}
.btn{background:var(--navy);color:#fff;font-size:14px;font-weight:600;width:166px;height:50px;display:flex;align-items:center;justify-content:center}

/* partners */
.partner{top:2332px;height:70px}
.map{top:2477px;left:0;width:1200px;height:306px;background:linear-gradient(120deg,#c7dcea 0%,#e7e3d6 28%,#efe9d9 50%,#d9d3c2 70%,#e9e5d8 100%)}

/* footer */
.footer{top:2783px;left:0;width:1200px;height:337px;background:var(--footer)}
.fcol{top:2823px}
.fcol h6{font-size:16px;font-weight:600;color:var(--orange);margin-bottom:14px}
.fcol li{list-style:none;font-size:12px;line-height:22px;color:var(--footer-text)}
.copyright{top:3072px;left:0;width:1200px;text-align:center;font-size:12px;color:#ccc}
.copyright span{color:var(--orange)}
</style>
</head>
<body>

<header>
  <div class="abs brand"><span class="brand-dot"></span><span class="brand-name">VELMOT</span></div>
  <div class="abs social"><span></span><span></span><span></span></div>
  <div class="abs lang">EN</div>
  <div class="abs contact-line">
    <span><svg width="14" height="14" viewBox="0 0 24 24"><path fill="#1c2a6e" d="M6.6 10.8a15 15 0 0 0 6.6 6.6l2.2-2.2c.3-.3.7-.4 1-.2 1.1.4 2.3.6 3.6.6.6 0 1 .4 1 1V20c0 .6-.4 1-1 1A17 17 0 0 1 3 4c0-.6.4-1 1-1h3.5c.6 0 1 .4 1 1 0 1.3.2 2.5.6 3.6.1.3 0 .7-.2 1z"/></svg>+971 4 555 0142</span>
    <span><svg width="16" height="12" viewBox="0 0 16 12"><rect width="16" height="12" fill="#1c2a6e"/><path d="M0 0l8 6 8-6" stroke="#fff" stroke-width="1.3" fill="none"/></svg>info@velmot.com</span>
  </div>
  <nav class="abs nav">
    <a class="active">HOME</a><a>ABOUT</a><a>STUDENTS</a><a>OUR TEAM</a><a>SERVICES</a><a>MEDIA</a><a>FAQ</a><a>LINKS</a><a>EVENTS</a><a>LOCATION</a>
  </nav>
</header>

<section class="abs hero" role="img" aria-label="Smiling graduate student in a cap with classmates behind her">
  <div class="abs hero-arrow" style="left:24px"><svg width="38" height="38" viewBox="0 0 38 38"><path d="M22 11l-8 8 8 8" stroke="#fff" stroke-width="3" fill="none"/></svg></div>
  <div class="abs hero-arrow" style="left:1134px"><svg width="38" height="38" viewBox="0 0 38 38"><path d="M16 11l8 8-8 8" stroke="#fff" stroke-width="3" fill="none"/></svg></div>
  <div class="abs hero-caption">We Guide and<br>Empower Students</div>
  <svg class="abs hero-curve" width="1200" height="40" viewBox="0 0 1200 40"><path d="M0 40 Q600 -20 1200 40Z" fill="#fff"/></svg>
</section>

<section>
  <div class="abs feature" style="left:100px">
    <div class="feature-head"><span class="feature-icon"><svg width="20" height="20" viewBox="0 0 20 20"><circle cx="10" cy="6" r="4.5" fill="#fff"/><path d="M2 19c0-5 3.5-7 8-7s8 2 8 7z" fill="#fff"/></svg></span><h3>About Us</h3></div>
    <p class="tag">Your US University Specialists in the GCC</p>
    <p class="body">When you engage us, you have access to an entire team of American university professionals [...]</p>
    <a class="more">READ MORE &nbsp;»</a>
  </div>
  <div class="abs feature" style="left:443px">
    <div class="feature-head"><span class="feature-icon"><svg width="22" height="18" viewBox="0 0 22 18"><path d="M1 4h5l8 10h6M1 14h5l8-10h6" stroke="#fff" stroke-width="2" fill="none"/><path d="M17 1l4 3-4 3M17 11l4 3-4 3" stroke="#fff" stroke-width="2" fill="none"/></svg></span><h3>Agent or a Consultant ?</h3></div>
    <p class="tag">We are independent educational consultants - Not agents</p>
    <p class="body">We are not commissioned agents working on behalf of any universities [...]</p>
    <a class="more">READ MORE &nbsp;»</a>
  </div>
  <div class="abs feature" style="left:788px">
    <div class="feature-head"><span class="feature-icon"><svg width="20" height="20" viewBox="0 0 20 20"><rect x="1" y="8" width="4" height="11" fill="#fff"/><path d="M7 9l4-8c2 0 2.5 1.5 2 4h5c1 0 1.5 1 1.2 2l-2 9c-.2.8-.8 1-1.5 1H7z" fill="none" stroke="#fff" stroke-width="1.6"/></svg></span><h3>Our Success Story</h3></div>
    <p class="tag">Universities to which our students have been admitted</p>
    <p class="body">To guide and empower students seeking to realize their maximum personal, academic,[...]</p>
    <a class="more">READ MORE &nbsp;»</a>
  </div>
</section>

<div class="abs rule" style="top:911px"></div>

<section>
  <h2 class="abs section-title" style="left:100px;top:934px">Our Services</h2>
  <a class="abs btn-small" style="left:1017px;top:943px">VIEW ALL</a>
  <div class="abs service" style="left:98px">
    <div class="service-photo" role="img" aria-label="Sprinters crouched at the starting line of a track" style="background:linear-gradient(160deg,#7a3a2a,#c98c6a 45%,#b44a3a 75%,#8a6a5a)"></div>
    <h4>SPORTS PACKAGE</h4>
    <p>15 Academic Counselling Sessions Unlimited Highlight Video Editing Promotion and Communication [...]</p>
    <a class="more">READ MORE &nbsp;»</a>
  </div>
  <div class="abs service" style="left:356px">
    <div class="service-photo" role="img" aria-label="Group of smiling university students holding books" style="background:linear-gradient(160deg,#d8c2a8,#c07890 40%,#f0f0f0 60%,#7aa04a 85%)"></div>
    <h4>PHD/MBA/JD</h4>
    <p>One-on-One Counseling Up to 8 Applications Multiple Personal Statement Brainstorming [...]</p>
    <a class="more">READ MORE &nbsp;»</a>
  </div>
  <div class="abs service" style="left:614px">
    <div class="service-photo" role="img" aria-label="Graduate in cap and gown giving a thumbs up" style="background:linear-gradient(160deg,#3a5a3a,#6a8a5a 40%,#1a1a1a 65%,#4a6a4a)"></div>
    <h4>MS/MA</h4>
    <p>One-on-One Counseling Up to 8 Applications Multiple Personal Statement Brainstorming [...]</p>
    <a class="more">READ MORE &nbsp;»</a>
  </div>
  <div class="abs service" style="left:870px">
    <div class="service-photo" role="img" aria-label="Student with a backpack in front of a campus building" style="background:linear-gradient(160deg,#a86a4a,#d8b8a0 40%,#e07aa0 65%,#9a7a6a)"></div>
    <h4>TRUE BLUE PACKAGE</h4>
    <p>One-on-One CounselingAssistance with the Shared Application Only Personal Statement Brainstorming [...]</p>
    <a class="more">READ MORE &nbsp;»</a>
  </div>
</section>

<div class="abs rule" style="top:1375px"></div>

<section>
  <h2 class="abs section-title" style="left:100px;top:1406px">Our News</h2>
  <div class="abs news-item" style="top:1484px">
    <h4>Neque porro quisquam est qui dolorem</h4>
    <div class="news-date"><svg width="14" height="14" viewBox="0 0 14 14"><rect x="1" y="2" width="12" height="11" fill="none" stroke="#d99a22" stroke-width="1.5"/><rect x="1" y="2" width="12" height="3" fill="#d99a22"/></svg>05/05/2015</div>
    <p>Lorem Ipsum is simply dummy text of the printing and typesetting industry. Lorem Ipsum has been the industry's standard dummy .</p>
    <a class="more">READ MORE &nbsp;»</a>
  </div>
  <div class="abs news-item" style="top:1638px">
    <h4>Neque porro quisquam est qui dolorem</h4>
    <div class="news-date"><svg width="14" height="14" viewBox="0 0 14 14"><rect x="1" y="2" width="12" height="11" fill="none" stroke="#d99a22" stroke-width="1.5"/><rect x="1" y="2" width="12" height="3" fill="#d99a22"/></svg>05/05/2015</div>
    <p>Lorem Ipsum is simply dummy text of the printing and typesetting industry. Lorem Ipsum has been the industry's standard dummy .</p>
    <a class="more">READ MORE &nbsp;»</a>
  </div>

  <h2 class="abs section-title" style="left:601px;top:1406px">Testimonials</h2>
  <div class="abs testimonial" style="top:1485px">
    <div class="testimonial-photo" role="img" aria-label="Portrait of a client in a suit" style="background:linear-gradient(160deg,#4a4a4a,#b08a70 50%,#2a2a30)"></div>
    <div><h5>Aaron Whitley</h5><p>" Sed ut perspiciatis unde omnis iste natus error sit voluptatem accusantium doloremque laudantium, totam rem aperiam, eaque ipsa quae ab illo inventore. "</p></div>
  </div>
  <div class="abs testimonial" style="top:1641px">
    <div class="testimonial-photo" role="img" aria-label="Portrait of a smiling client" style="background:linear-gradient(160deg,#e0e0e0,#7a5040 50%,#d8d0d0)"></div>
    <div><h5>Aaron Whitley</h5><p>" Sed ut perspiciatis unde omnis iste natus error sit voluptatem accusantium doloremque laudantium, totam rem aperiam, eaque ipsa quae ab illo inventore. "</p></div>
  </div>
</section>

<div class="abs rule" style="top:1812px"></div>

<section>
  <div class="abs video" role="img" aria-label="Video still of graduates throwing caps in front of a columned hall">
    <svg class="abs" style="left:208px;top:109px" width="48" height="48" viewBox="0 0 48 48"><circle cx="24" cy="24" r="24" fill="#d8141c"/><path d="M19 14l14 10-14 10z" fill="#1a1a1a"/></svg>
  </div>
  <div class="abs admit">
    <h2>University to which our students have been admitted</h2>
    <p>Sed ut perspiciatis unde omnis iste natus error sit voluptatem accusantium doloremque laudantium, totam rem aperiam, eaque ipsa quae &nbsp;illo inventore veritatis quasi architecto beatae vitae dicta sunt explicabo. Nemo enim ipsam voluptatem quia voluptas sit aspernatur.</p>
    <a class="btn">CHECK THE LIST</a>
  </div>
</section>

<div class="abs rule" style="top:2190px"></div>

<section>
  <h2 class="abs section-title" style="left:100px;top:2238px">Our Partners</h2>
  <a class="abs btn-small" style="left:1017px;top:2246px">VIEW ALL</a>
  <svg class="abs" style="left:98px;top:2354px" width="20" height="26" viewBox="0 0 20 26"><path d="M16 2L5 13l11 11" stroke="#b07a1e" stroke-width="5" fill="none"/></svg>
  <svg class="abs" style="left:1082px;top:2354px" width="20" height="26" viewBox="0 0 20 26"><path d="M4 2l11 11L4 24" stroke="#b07a1e" stroke-width="5" fill="none"/></svg>
  <div class="abs partner" style="left:156px;width:88px;border-radius:50%;background:#7aa63a"></div>
  <div class="abs partner" style="left:306px;width:120px;top:2352px;height:32px;background:#e8b01a"></div>
  <div class="abs partner" style="left:506px;width:128px;background:#111"></div>
  <div class="abs partner" style="left:702px;width:132px;top:2342px;height:52px;background:#555"></div>
  <div class="abs partner" style="left:926px;width:108px;top:2350px;height:34px;background:#c8a0a0"></div>
</section>

<section class="abs map" role="img" aria-label="Street map of the city with a location pin at the beach"></section>

<footer>
  <div class="abs footer"></div>
  <div class="abs fcol" style="left:102px"><h6>Academics</h6><ul><li>Admissions</li><li>Departments</li><li>Classes &amp; Homework</li><li>Staff Directory</li><li>Guidance</li><li>College Office</li><li>Library</li><li>Schedule</li></ul></div>
  <div class="abs fcol" style="left:354px"><h6>Courses</h6><ul><li>Dolor sit amet</li><li>Ctetur adipisicing</li><li>Elit sed do eiusmod</li><li>Incididunt ut labore</li><li>Et dolore magna</li><li>Ut enim ad minim</li><li>Quis nostrud</li></ul></div>
  <div class="abs fcol" style="left:605px"><h6>Events</h6><ul><li>Dolor sit amet</li><li>Ctetur adipisicing</li><li>Elit sed do eiusmod</li><li>Incididunt ut labore</li><li>Et dolore magna</li></ul></div>
  <div class="abs fcol" style="left:900px"><h6>Contact Us</h6><ul><li>The Harbor Point Office Building</li><li>Suite 512 – Fifth Floor</li><li>Coral Bay Road</li><li>P.O Box 40217</li><li>Dubai, United Arab Emirates</li></ul></div>
  <p class="abs copyright"><span>Velmot</span> © 2015. All rights are reserved.</p>
</footer>

</body>
</html>
```